Kelvane Plumbing Business cards

Company is Kelvane Plumbing.
name Dashel Morrowby, I am a plumber, drainer, gasfitter and roofer
Mobile: 0431 906 154
Email address: info@kelvaneplumbing.example (check out my website for some ideas)
Website: www.kelvaneplumbing.example
ABN: 82 916 203 471
LIC: 604517K

I am reliable all round plumber. I am a 24 hour emergency service. Kelvane Plumbing is a professional plumbing service in the Illawarra, South Coast, Southern Sydney and Southern Highland regions of NSW. We offer a 24 hour emergency service for piece of mind to our customers. Call us now to see how we can help you. Kelvane Plumbing approaches every job with attention to detail and excellent customer service. With our superior workmanship you can be confident that the job will be done right the first time around. You can rest assured with results that are guaranteed to last.

Target Market(s)

the general public

Contact Information for Business Card

look up website for some ideas something with similar colours to logo and new modern and to catch the eye.

Colors
fdfdfd
ffffff
000000
7f7f7f
aaaaaa
33a6d7
0492cd

Requirements
Must have
• all contact details
• company- Kelvane Plumbing
• name- Dashel Morrowby
• number mobile- 0431 906 154
• Email address- info@kelvaneplumbing.example
• Website- www.kelvaneplumbing.example
• ABN- 82 916 203 471
• LIC- 604517K

```html
<!DOCTYPE html>
<html lang="en">
<head>
<meta charset="utf-8">
<title>Kelvane Plumbing Business Cards</title>
<link href="https://fonts.googleapis.com/css2?family=Questrial&family=Hind:wght@400;600;700&display=swap" rel="stylesheet">
<style>
  :root {
    --ink: #000000;
    --panel: #e3e3e3;
    --paper: #ffffff;
    --grey: #7f7f7f;
    --blue: #33a6d7;
    --text: #1a1a1a;
    --icon: #141a22;
  }
  * { margin: 0; padding: 0; box-sizing: border-box; }
  html, body { width: 932px; height: 1200px; overflow: hidden; background: var(--paper); }
  .canvas { position: relative; width: 932px; height: 1200px; }

  .card { position: absolute; left: 0; width: 932px; overflow: hidden; }
  .card--front { top: 0; height: 570px; border-bottom: 2px solid var(--ink); }
  .card--back { top: 627px; height: 573px; border-top: 2px solid var(--ink); }

  .panel { position: absolute; top: 0; bottom: 0; }
  .panel--light { background: var(--panel); }
  .panel--dark { background: var(--ink); }
  .card--front .panel--light { left: 0; width: 339px; }
  .card--front .panel--dark { left: 339px; right: 0; }
  .card--back .panel--dark { left: 0; width: 339px; }
  .card--back .panel--light { left: 339px; right: 0; }

  .website {
    position: absolute;
    font-family: "Questrial", sans-serif;
    color: var(--text);
    white-space: nowrap;
    transform: translate(-50%, -50%) rotate(-90deg);
  }
  .website--front { left: 168px; top: 285px; font-size: 30px; }
  .website--back { left: 898px; top: 912px; font-size: 28px; position: fixed; }

  .brand {
    position: absolute;
    font-family: "Hind", sans-serif;
    font-weight: 700;
    color: var(--blue);
    text-align: center;
    letter-spacing: 1px;
    line-height: 1.05;
  }
  .brand--front { left: 440px; top: 200px; width: 384px; font-size: 50px; }
  .brand-mark {
    display: block;
    margin: 0 auto 18px;
    width: 26px; height: 26px;
    border-radius: 50%;
    background: var(--blue);
  }
  .brand--back {
    left: 83px; top: 200px; width: 174px; font-size: 26px;
    transform: rotate(-90deg);
  }

  .person { position: absolute; left: 364px; top: 682px; font-family: "Hind", sans-serif; color: var(--text); }
  .person__name { font-size: 36px; font-weight: 700; line-height: 1; }
  .person__role { margin-top: 8px; font-size: 20px; font-weight: 400; }

  .contacts { position: absolute; left: 364px; top: 799px; list-style: none; }
  .contact { display: flex; align-items: center; height: 56px; margin-bottom: 35.5px; }
  .contact__icon {
    width: 56px; height: 56px; border-radius: 50%;
    background: var(--icon);
    display: flex; align-items: center; justify-content: center;
    color: var(--paper);
    font-family: "Hind", sans-serif; font-size: 20px; font-style: italic;
    flex-shrink: 0;
  }
  .contact__text {
    margin-left: 10px;
    font-family: "Questrial", sans-serif;
    font-size: 23px;
    color: var(--text);
  }
</style>
</head>
<body>
<div class="canvas">

  <section class="card card--front">
    <div class="panel panel--light"></div>
    <div class="panel panel--dark"></div>
    <p class="website website--front">www.kelvaneplumbing.example</p>
    <p class="brand brand--front"><span class="brand-mark"></span>KELVANE<br>PLUMBING</p>
  </section>

  <section class="card card--back">
    <div class="panel panel--dark"></div>
    <div class="panel panel--light"></div>
    <p class="brand brand--back">KELVANE<br>PLUMBING</p>
  </section>

  <div class="person">
    <h1 class="person__name">Dashel Morrowby</h1>
    <p class="person__role">Plumber, Drainer, Gasfitter and roofer</p>
  </div>

  <ul class="contacts">
    <li class="contact">
      <span class="contact__icon">
        <svg width="18" height="30" viewBox="0 0 18 30" aria-hidden="true">
          <rect x="1.5" y="1.5" width="15" height="27" rx="3" fill="none" stroke="#ffffff" stroke-width="2"/>
          <line x1="6" y1="24" x2="12" y2="24" stroke="#ffffff" stroke-width="2"/>
        </svg>
      </span>
      <span class="contact__text">0431 906 154</span>
    </li>
    <li class="contact">
      <span class="contact__icon">
        <svg width="30" height="22" viewBox="0 0 30 22" aria-hidden="true">
          <rect x="1" y="1" width="28" height="20" fill="#ffffff"/>
          <polyline points="1,1 15,12 29,1" fill="none" stroke="#141a22" stroke-width="1.5"/>
          <polyline points="1,21 11,9" fill="none" stroke="#141a22" stroke-width="1"/>
          <polyline points="29,21 19,9" fill="none" stroke="#141a22" stroke-width="1"/>
        </svg>
      </span>
      <span class="contact__text">info@kelvaneplumbing.example</span>
    </li>
    <li class="contact">
      <span class="contact__icon">ABN</span>
      <span class="contact__text">82 916 203 471</span>
    </li>
    <li class="contact">
      <span class="contact__icon">LIC</span>
      <span class="contact__text">604517K</span>
    </li>
  </ul>

  <p class="website website--back">www.kelvaneplumbing.example</p>

</div>
</body>
</html>
```